van Kalder Jewelry & Co. needs a website design

We need a website design for a new company based in Minnesota called 'van Kalder Jewelry & Co.' My wife and I are both geologists who handcraft fine jewelry using nephrite-jade from a newly discovered glacial deposit in Minnesota that I independently discovered, researched, and extracted. The jade colors range from a beautiful black to dark green and are mostly set in yellow gold, though we also use silver, platinum, and white gold. We will also be using nephrite-jade, jadeite-jade's from other parts of the world, including other semi- precious and precious stones such as black onyx/ chalcedony's, rubies ,sapphire, and diamonds. The family name 'van Kalder' means of the ash tree in French, and I would this motif to be incorporated into the website design. I've attached the files for our company logo and would like to blend that theme and emblem into the design as well in an elegant fashion. I'm aiming for a black jade/ dark green and yellow gold look am primarily interested in a design optimized for online shoppers. Additionally, I want a section where visitors can read a brief summary of our research and discovery story as geologists. Currently, we will be selling pendant necklaces, bead necklaces, earrings, bead bracelets, and bracelets. The website should convey that we sell fine, handcrafted, and very unique jewelry.

```html
<!DOCTYPE html>
<html lang="en">
<head>
<meta charset="utf-8">
<title>van Kalder Jewelry &amp; Co.</title>
<link rel="stylesheet" href="https://fonts.googleapis.com/css2?family=Gilda+Display&family=Jost:wght@400;500&display=swap">
<style>
:root{
  --gold:#c9a94b;
  --gold-light:#d8c46a;
  --forest:#1f4511;
  --forest-mid:#4a8a5c;
  --ink:#141414;
  --black:#000;
  --paper:#fff;
  --muted:#555;
  --serif:'Gilda Display', serif;
  --sans:'Jost', sans-serif;
}
*{margin:0;padding:0;box-sizing:border-box}
html,body{width:1200px;height:4167px;overflow:hidden}
body{position:relative;background:var(--paper);font-family:var(--sans);color:var(--ink)}
.abs{position:absolute}
.ph{position:absolute;overflow:hidden}

.promo-bar{left:0;top:0;width:1200px;height:32px;background:var(--gold);color:#fff;font-size:11px;font-weight:500;letter-spacing:.8px;text-align:center;line-height:32px}

.hero{left:0;top:32px;width:1200px;height:672px;background:var(--black)}
.hero-photo{left:348px;top:0;width:852px;height:672px;background:radial-gradient(ellipse at 55% 55%,#2f6a44 0%,#153a25 35%,#0b1a12 65%,#000 100%)}
.brand-box{left:142px;top:0;width:162px;height:133px;background:#0c0c0c;display:flex;flex-direction:column;align-items:center;justify-content:center;gap:8px}
.brand-mark{width:34px;height:34px;border:2px solid var(--gold)}
.brand-name{font-family:var(--serif);color:var(--gold);font-size:16px;letter-spacing:1.5px;text-align:center;line-height:1.2}
.main-nav{left:410px;top:36px;display:flex;gap:30px}
.main-nav a{color:#fff;font-size:11px;letter-spacing:.8px;text-decoration:none;display:flex;align-items:center;gap:8px}
.main-nav a::before{content:"";width:18px;height:1px;background:var(--gold)}
.account{left:940px;top:36px;color:#fff;font-size:11px;letter-spacing:.6px}
.cart{left:1083px;top:28px}
.hero-title{left:86px;top:268px;font-family:var(--serif);color:#fff;font-size:44px;line-height:50px;font-weight:400}
.hero-title span{color:var(--gold-light)}
.hero-btn{left:89px;top:400px;width:184px;height:40px;background:var(--gold);color:#fff;font-size:11px;letter-spacing:1px;display:flex;align-items:center;gap:14px;padding-left:12px;box-shadow:4px 4px 0 -1px #000,5px 5px 0 0 var(--gold)}
.hero-btn::before{content:"";width:30px;height:1px;background:#fff}

.section-title{font-family:var(--serif);font-size:30px;font-weight:400}
.bestsellers-title{left:139px;top:766px}
.arrows{left:1010px;top:766px;display:flex;gap:28px;font-size:18px;color:#333}
.side-tab{left:1184px;top:1019px;width:40px;height:283px;background:var(--gold);border-radius:30px 0 0 30px}
.product{width:216px;text-align:center}
.product .ph{left:50%;transform:translateX(-50%);top:0;width:70px;height:178px}
.product .sale{position:absolute;top:6px;right:44px;background:var(--gold-light);font-size:11px;padding:3px 8px}
.product .name{position:absolute;top:194px;left:0;width:216px;font-size:11.5px;line-height:16px;color:#333}
.product .price{position:absolute;top:252px;left:0;width:216px;font-size:12.5px;font-weight:500;letter-spacing:.5px}

.category-band{left:0;top:1226px;width:1200px;height:840px}
.category-title{left:0;top:1290px;width:1200px;text-align:center;color:#fff}
.cat-label{color:#fff;font-size:17px;text-align:center;width:215px}
.dark-btn{background:var(--black);color:#fff;font-size:11px;letter-spacing:1px;display:flex;align-items:center;justify-content:center}

.eyebrow{color:var(--forest);font-size:13px;font-weight:500}
.history-title{left:145px;top:1900px;font-family:var(--serif);font-size:50px;line-height:57px;letter-spacing:-1px;font-weight:400;width:720px}
.tabs{left:147px;top:2154px;display:flex;gap:40px;font-size:14px;font-weight:500;color:var(--forest)}
.tabs .active{border-bottom:2px solid var(--forest);padding-bottom:6px}
.history-copy{left:146px;top:2198px;width:370px;font-size:13.4px;line-height:19.5px;color:var(--muted)}

.gem-heading{left:720px;top:2808px;font-family:var(--serif);font-size:44px;line-height:49px;font-weight:400}
.gem-heading span{color:var(--forest)}
.gem-rule{left:720px;top:2921px;width:145px;height:2px;background:var(--forest)}
.gem-copy{left:726px;top:2952px;width:320px;font-size:13px;line-height:20px;color:var(--muted)}
.outline-btn{left:726px;top:3049px;width:224px;height:38px;border:1px solid #333;font-size:11px;letter-spacing:.5px;display:flex;align-items:center;justify-content:center;color:#333}
.gem{width:110px;text-align:center;font-size:11px;font-weight:500;letter-spacing:.3px}
.gem .stone{width:46px;height:40px;margin:0 auto 10px;border-radius:50%}

.craft-title{left:159px;top:3316px;font-family:var(--serif);font-size:47px;line-height:49px;letter-spacing:-1px;color:var(--forest);font-weight:400}
.craft-sub{left:161px;top:3437px;font-family:var(--serif);font-size:22px}

.footer-head{font-family:var(--serif);color:var(--gold);font-size:17px;letter-spacing:.5px}
.footer-links{list-style:none;font-size:11.5px;letter-spacing:.6px;color:#fff;line-height:23px;font-weight:500}
.footer-note{color:#fff;font-size:11.5px;letter-spacing:.6px;line-height:16px}
</style>
</head>
<body>

<div class="abs promo-bar">ENJOY COMPLIMENTARY 2-5 DAYS SHIPPING &amp; EASY RETURNS</div>

<header class="abs hero">
  <div class="ph hero-photo" role="img" aria-label="Carved green jade pendant beside a strand of jade beads on a dark background"></div>
  <div class="abs brand-box">
    <div class="brand-mark"></div>
    <div class="brand-name">VAN KALDER<br><span style="font-size:11px;letter-spacing:2px">JEWELRY &amp; CO.</span></div>
  </div>
  <nav class="abs main-nav">
    <a href="#">HOME</a><a href="#">ABOUT US</a><a href="#">COLLECTIONS</a><a href="#">CONTACT</a>
  </nav>
  <div class="abs account">REGISTER / LOGIN</div>
  <svg class="abs cart" width="50" height="32" viewBox="0 0 50 32" aria-hidden="true">
    <path d="M2 11h4l3 11h12l3-8H8" fill="none" stroke="#fff" stroke-width="1.5"/>
    <circle cx="11" cy="26" r="1.6" fill="#fff"/><circle cx="19" cy="26" r="1.6" fill="#fff"/>
    <circle cx="38" cy="10" r="9" fill="var(--gold)"/>
    <text x="38" y="14" text-anchor="middle" font-size="10" fill="#fff" font-family="Jost, sans-serif">0</text>
  </svg>
  <h1 class="abs hero-title">Exquisite Handmade<br><span>Jade Jewelry.</span></h1>
  <div class="abs hero-btn">EXPLORE NOW</div>
</header>

<h2 class="abs section-title bestsellers-title">Best Selling Products</h2>
<div class="abs arrows"><span>&#8249;</span><span>&#8250;</span></div>
<div class="abs side-tab"></div>

<div class="abs product" style="left:137px;top:865px">
  <div class="ph" role="img" aria-label="Black jade pendant on a gold chain" style="background:linear-gradient(#e9dcc0 0 55%,#1e2a22 55%)"></div>
  <span class="sale">Sale</span>
  <p class="name">18k Rose Gold Natural Imperial Green Oval Jadeite Jade Engagement Ring With Diamonds</p>
  <p class="price">RS. 836,300.00</p>
</div>
<div class="abs product" style="left:374px;top:865px">
  <div class="ph" role="img" aria-label="Carved black jade pendant on a gold chain" style="background:linear-gradient(#e9dcc0 0 50%,#1a1d1a 50%)"></div>
  <span class="sale">Sale</span>
  <p class="name">18k Rose Gold Natural Imperial Green Oval Jadeite Jade Engagement Ring With Diamonds</p>
  <p class="price">RS. 836,300.00</p>
</div>
<div class="abs product" style="left:608px;top:865px">
  <div class="ph" role="img" aria-label="Green jade teardrop pendant on a white gold chain" style="background:linear-gradient(#e0e0e0 0 60%,#7cc24a 60%)"></div>
  <span class="sale">Sale</span>
  <p class="name">Lakeview 18k White Gold Natural Imperial Green Jadeite Jade Engagement Ring With Diamonds</p>
  <p class="price">RS. 836,300.00</p>
</div>
<div class="abs product" style="left:855px;top:865px">
  <div class="ph" role="img" aria-label="Dark green jade pendant on a gold chain" style="background:linear-gradient(#e9dcc0 0 55%,#1c2a20 55%)"></div>
  <p class="name">18k Rose Gold Natural Imperial Green Oval Jadeite Jade Engagement Ring With Diamonds</p>
  <p class="price">RS. 836,300.00</p>
</div>

<svg class="abs category-band" viewBox="0 0 1200 840" preserveAspectRatio="none" aria-hidden="true">
  <path d="M0 0H1200V829C1080 835 1000 800 930 730C870 670 800 600 690 570C580 545 520 600 420 575C320 550 240 520 140 540C80 552 30 560 0 553Z" fill="var(--forest)"/>
</svg>
<h2 class="abs section-title category-title">Shop By Category</h2>
<div class="ph" role="img" aria-label="Gold necklace with a small jade drop worn on the neck" style="left:136px;top:1383px;width:217px;height:205px;border-radius:0 16px 16px 16px;background:linear-gradient(135deg,#f0dcc6,#c99b7a)"></div>
<div class="ph" role="img" aria-label="Jade cabochon ring resting on stone" style="left:374px;top:1391px;width:215px;height:200px;border-radius:50%;background:linear-gradient(#7a5a45 0 45%,#d9cfc4 45%)"></div>
<div class="ph" role="img" aria-label="Wrist wearing stacked jade bead bracelets" style="left:612px;top:1375px;width:215px;height:210px;border-radius:110px 110px 0 0;background:linear-gradient(#dcb9a0 0 55%,#2f6c3e 55%)"></div>
<svg class="abs" style="left:840px;top:1385px" width="232" height="220" viewBox="0 0 232 220" role="img" aria-label="Woman wearing green drop earrings">
  <path d="M40 10C80 30 110 40 140 20C170 5 230 0 230 40C230 80 160 90 170 150C178 200 140 220 110 190C80 160 40 180 10 170C0 160 40 120 40 80C40 50 20 0 40 10Z" fill="#c9a48a"/>
</svg>
<div class="abs cat-label" style="left:120px;top:1600px">Necklaces</div>
<div class="abs cat-label" style="left:362px;top:1600px">Rings</div>
<div class="abs cat-label" style="left:612px;top:1601px">Bead Bracelets</div>
<div class="abs cat-label" style="left:815px;top:1601px">Ear Rings</div>
<div class="abs dark-btn" style="left:495px;top:1677px;width:210px;height:41px">VIEW OUR COLLECTIONS</div>

<p class="abs eyebrow" style="left:147px;top:1866px">Our History</p>
<h2 class="abs history-title">All of our jade is handmade with fairmined gold in our workshop in France</h2>
<div class="abs tabs"><span class="active">Our Research</span><span>Our Story</span></div>
<p class="abs history-copy">Lorem ipsum dolor sit amet, consectetl adipisicing elit, sed do eiusmod tempor incididul ut labore et dolore magna aliqua. Ut enim ad minim veniam, quis nostrud. Lorem ipsum dolor sit amet consectetu to adipisicing elit sed do eius.The product is created entirely by fine craftsmanship through the hands and artistic mind of the artisan.Each handicraft product has its own nuance of each craft village and each artisan…Lorem ipsum dolor sit amet, consectetl adipisicing elit, sed do eiusmod tempor incididul ut labore et dolore magna aliqua. Ut enim ad minim veniam, quis nostrud</p>
<div class="ph" role="img" aria-label="Pair of speckled jade drop earrings on a leaf" style="left:597px;top:2088px;width:254px;height:277px;border-radius:30px 30px 0 30px;background:linear-gradient(135deg,#b8cf8c,#6f7d3a)"></div>
<div class="ph" role="img" aria-label="Long jade drop earring worn beside a leaf" style="left:862px;top:2046px;width:238px;height:267px;border-radius:24px 0 24px 0;background:linear-gradient(135deg,#2c5a33,#c59276)"></div>
<div class="ph" role="img" aria-label="Raw green jade pieces on stones among leaves" style="left:721px;top:2329px;width:402px;height:275px;border-radius:40px 40px 40px 40px;background:radial-gradient(ellipse at 45% 60%,#1f7a52,#0f1a14 70%)"></div>

<div class="abs" style="left:144px;top:2687px;width:469px;height:18px;background:var(--gold-light)"></div>
<div class="abs" style="left:0;top:2750px;width:110px;height:407px;background:var(--forest-mid)"></div>
<div class="ph" role="img" aria-label="Woman in a blue satin dress wearing a sapphire necklace, ring and bracelet" style="left:108px;top:2705px;width:547px;height:514px;background:linear-gradient(135deg,#1a2233,#2a4a8f 55%,#c49a82)"></div>
<p class="abs eyebrow" style="left:723px;top:2775px;font-size:12px">Semi- Precious and Precious Stones</p>
<h2 class="abs gem-heading">Unique and brilliant<br><span>Gemstone Jewelry</span></h2>
<div class="abs gem-rule"></div>
<p class="abs gem-copy">Perfect Match for Every Occasion. Coordinate with other pieces from the collection for a classic look.</p>
<div class="abs outline-btn">EXPLORE OUR COLLECTIONS</div>
<div class="abs gem" style="left:694px;top:3130px"><div class="stone" style="background:#b0142c"></div>RUBIES</div>
<div class="abs gem" style="left:801px;top:3130px"><div class="stone" style="background:#2a3a9a"></div>SAPPHIRE</div>
<div class="abs gem" style="left:914px;top:3130px"><div class="stone" style="background:#d9dee6"></div>DIAMONDS</div>
<div class="abs gem" style="left:1016px;top:3130px"><div class="stone" style="background:#3a3a3a"></div>ONYX/<br>CHALCEDONY</div>

<h2 class="abs craft-title">We sell fine, handcrafted, and very<br>unique jewelry.</h2>
<p class="abs craft-sub">Imperial Jade Collection</p>
<div class="abs dark-btn" style="left:165px;top:3487px;width:171px;height:42px">SHOP NOW</div>
<div class="ph" role="img" aria-label="Rose gold earrings with pale jade beads on a white stand" style="left:430px;top:3450px;width:291px;height:290px;border-radius:36px;background:linear-gradient(135deg,#f3eeea,#d6cfc8)"></div>
<div class="ph" role="img" aria-label="Silver hoop earrings with dark green jade beads on a white stand" style="left:749px;top:3418px;width:370px;height:354px;border-radius:36px;background:linear-gradient(135deg,#efefed,#cfd0cc)"></div>

<svg class="abs" style="left:0;top:3680px" width="1200" height="487" viewBox="0 0 1200 487" aria-hidden="true">
  <path d="M0 10C120 50 200 130 320 180C440 230 520 260 640 250C760 240 820 200 900 175C1000 145 1100 150 1200 140V487H0Z" fill="var(--forest)"/>
</svg>
<h3 class="abs footer-head" style="left:222px;top:3968px">Informations</h3>
<ul class="abs footer-links" style="left:222px;top:3996px"><li>ABOUT VAN KALDER JEWELRY</li><li>FAQS</li><li>CONTACT US</li></ul>
<h3 class="abs footer-head" style="left:453px;top:3968px">Policies</h3>
<ul class="abs footer-links" style="left:453px;top:3996px"><li>SHIPPING</li><li>PRIVACY POLICY</li><li>RETURNS &amp; EXCHANGES</li></ul>
<h3 class="abs footer-head" style="left:768px;top:3974px">Join our mailing list</h3>
<div class="abs footer-note" style="left:770px;top:4034px">Enter email</div>
<div class="abs" style="left:768px;top:4055px;width:296px;height:1px;background:#fff"></div>
<svg class="abs" style="left:1034px;top:4036px" width="20" height="10" viewBox="0 0 20 10" aria-hidden="true"><path d="M0 5H18M14 1l4 4-4 4" fill="none" stroke="#fff" stroke-width="1.2"/></svg>
<p class="abs footer-note" style="left:770px;top:4076px;width:300px">Be the first to hear about our special promotions and new products.</p>
<p class="abs footer-note" style="left:136px;top:4127px">© 2024, VAN KALDER JEWELRY &amp; CO. All rights reserved.</p>

</body>
</html>
```